Captain Pebble - Book cover for a children's book

I need a book cover for a children's book size A 4 which can be used for print and ebook. The story has about 16,000 words and ten hand-made watercolor illustrations. One of these should be on the book cover (file provided). The design of the book cover should match the illustration.
The book is for children aged 6-10 years old.

Name of the book: Captain Pebble
written by: Tilda Vorhagen
illustrated by: Celeste Marina Dunn

Thank you!

Synopsis:
Captain Pebble is the story of a frustrated mouse who is the leader of a questing team, comprised of himself, a racoon, a slug, and a giraffe – Captain Pebble (ambitious, but with low self-esteem that he covers up by being bossy), Pippa Parrot (beautiful, forgetful, and unable to read), Wendy Worm (confident and strong, but extremely slow) and Oliver Otter (jolly and practical, yet single-mindedly focused on food). One of the many running jokes throughout the book is that Captain Pebble thinks Oliver is a pig, a confusion which is only resolved near the end of the book. Captain Pebble sees himself as the rightful leader of the team, as he is by far the smartest. He also fears he will not be successful in completing his quest, as he has been forced to team up with less than ideal quest teammates. During the team’s quest, Captain Pebble loses each of his team members, one by one. Following the revelation of her illiteracy, Pippa opts to stay behind at the first obstacle, Oliver runs off after apples for lunch, and Wendy gets distracted. Captain Pebble is excited to be able to go off on his own but gets snatched by an eagle. The other three team members band together to rescue Captain Pebble in haphazard circumstances. They all return to Quest school jubilant and ready to receive their diplomas, not realising that Captain Pebble will not qualify because he was the one who had to be rescued. When Captain Pebble does not get his diploma, the team come together and recall that during the rescue Captain Pebble had in fact also saved Wendy Worm, allowing them all to graduate together.
With so many different characteristics, the team show that they are stronger together than as individuals. By embracing their weaknesses and vulnerabilities they learn to cooperate and in the end this helps them to succeed. The team agree to stick together for future adventures.

Target Market(s)

Children 6-10 years old + their carers/grand-parents/ primary school teachers

Font styles to use
Serif
Sans Serif

Requirements
Must have
• Beautiful colors (matching the provided illustration), must have the provided illustration on the cover, must be appealing and heart-warming, spiking curiosity.

Must feature book name, name of author and name of illustrator.

Text for blurb on the back of the book cover:

"Captain Pebble tells the delightful story of four animals on a quest. These four could not be more different – there is a mouse, a giraffe, a slug, and a pig. But wait – is this really true? Captain Pebble, who thinks he is the leader, seems to have missed his zoology lessons at school.
There is more than one team competing to complete the quest. Can our odd team beat the lions? Who will be faster? Does being faster mean that you win? Find out what really matters in the end!"
Should not have
• should not be over-loaded, no large white spaces

```html
<!DOCTYPE html>
<html lang="en">
<head>
<meta charset="utf-8">
<title>Captain Pebble – Book Cover</title>
<link rel="stylesheet" href="https://fonts.googleapis.com/css2?family=Fondamento&family=Cinzel:wght@400&family=Crimson+Text&display=swap">
<style>
  :root {
    --paper: #ffffff;
    --cream: #fbefe6;
    --ink: #1c1a18;
    --teal: #1fb5a8;
    --sky: #3a7fc4;
    --navy: #2a4f9c;
    --leaf: #5fb86a;
    --meadow: #9fcf7a;
    --ochre: #d89a2a;
    --ember: #d8261f;
    --forest: #1d8a4a;
    --giraffe: #d9772a;
    --mist: #d9eee4;
  }
  * { box-sizing: border-box; margin: 0; padding: 0; }
  html, body {
    width: 1200px; height: 849px; overflow: hidden; background: var(--paper);
  }
  .cover-spread { position: relative; width: 1200px; height: 849px; background: var(--paper); }

  .panel { position: absolute; top: 0; height: 849px; overflow: hidden; }
  .panel--back { left: 0; width: 594px; }
  .panel--front { left: 604px; width: 596px; }

  .painted-ground { position: absolute; inset: 0; }
  .panel--back .painted-ground {
    background:
      radial-gradient(circle at 20% 30%, rgba(58,127,196,.55), transparent 45%),
      radial-gradient(circle at 80% 55%, rgba(42,79,156,.45), transparent 40%),
      linear-gradient(180deg, var(--teal) 0%, #2aa7b0 40%, var(--leaf) 75%, var(--meadow) 100%);
  }
  .panel--front .painted-ground {
    background:
      radial-gradient(circle at 60% 10%, rgba(29,138,74,.7), transparent 40%),
      linear-gradient(180deg, var(--teal) 0%, #2bb88e 35%, #3d9a68 58%, #8a4a2c 72%, var(--ember) 85%, #c81e1a 100%);
  }
  .painted-ground svg { position: absolute; inset: 0; width: 100%; height: 100%; }

  .title {
    position: absolute; font-family: "Fondamento", "Georgia", serif;
    color: var(--cream); font-weight: 400; line-height: .95; text-align: center;
    text-shadow: 0 1px 3px rgba(0,0,0,.25);
  }
  .title span { display: block; white-space: nowrap; }
  .title--back { left: 110px; width: 370px; top: 60px; font-size: 76px; }
  .title--back .line-two { padding-left: 40px; }
  .title--front { left: 40px; width: 236px; top: 560px; font-size: 54px; }
  .title--front .line-two { padding-left: 24px; }

  .rule { position: absolute; height: 0; border-top: 1.5px solid var(--cream); }
  .rule::after {
    content: ""; position: absolute; left: 50%; top: -5px; width: 8px; height: 8px;
    margin-left: -4px; border-radius: 50%; background: var(--cream);
  }
  .rule--back-top { left: 168px; width: 260px; top: 40px; }
  .rule--back-bottom { left: 168px; width: 260px; top: 270px; }
  .rule--front-top { left: 60px; width: 200px; top: 546px; }
  .rule--front-bottom { left: 60px; width: 200px; top: 718px; }

  .blurb {
    position: absolute; left: 88px; top: 318px; width: 414px; height: 414px;
    border-radius: 50%; background: var(--paper);
    padding-top: 28px; text-align: center;
  }
  .blurb p {
    font-family: "Crimson Text", "Georgia", serif;
    font-size: 16px; line-height: 22.6px; color: var(--ink);
  }
  .blurb .line { display: block; white-space: nowrap; }

  .code-panel {
    position: absolute; left: 52px; top: 730px; width: 126px; height: 81px; background: var(--paper);
  }

  .credits {
    position: absolute; left: 0; top: 30px; width: 596px; height: 84px;
    background: var(--paper); display: flex; flex-direction: column;
    justify-content: center; align-items: center; gap: 4px;
    font-family: "Cinzel", "Times New Roman", serif;
    letter-spacing: .5px; color: var(--ink); line-height: 1.15;
  }
  .credits .role { font-size: 19px; text-transform: uppercase; }

  .illustration { position: absolute; border-radius: 50%; }
  .illustration--giraffe {
    left: 12px; top: 128px; width: 360px; height: 360px;
    background: radial-gradient(circle at 45% 50%, var(--giraffe) 0%, #c9652a 35%, #a9cfc0 70%, var(--mist) 100%);
  }
  .illustration--mouse {
    left: 296px; top: 572px; width: 296px; height: 296px;
    background: radial-gradient(circle at 50% 55%, #8c8f94 0%, #c9d8b0 30%, #e6f0d6 65%, #b7d79a 100%);
  }
</style>
</head>
<body>
<main class="cover-spread">

  <section class="panel panel--back" aria-label="Back cover">
    <div class="painted-ground" role="img" aria-label="Swirling painted background in teal, blue and green with soft circles">
      <svg viewBox="0 0 594 849" aria-hidden="true">
        <circle cx="176" cy="200" r="148" fill="#2f5fae" opacity=".7"/>
        <circle cx="492" cy="64" r="108" fill="var(--ochre)" opacity=".9"/>
        <circle cx="16" cy="328" r="40" fill="#4a86c8" opacity=".6"/>
        <circle cx="40" cy="520" r="110" fill="#7fc99a" opacity=".5"/>
        <circle cx="470" cy="720" r="128" fill="#4d80c4" opacity=".45"/>
        <path d="M320 849 Q335 760 340 735 Q345 760 360 849 Z" fill="var(--ember)"/>
      </svg>
    </div>

    <div class="rule rule--back-top"></div>
    <h1 class="title title--back"><span>Captain</span><span class="line-two">Pebble</span></h1>
    <div class="rule rule--back-bottom"></div>

    <div class="blurb">
      <p>
        <span class="line">Captain Pebble tells the</span>
        <span class="line">delightful story of four animals</span>
        <span class="line">on a quest. These four could not be</span>
        <span class="line">more different – there is a mouse, a giraffe,</span>
        <span class="line">a slug, and a pig. But wait – is this really true?</span>
        <span class="line">Captain Pebble, who thinks he is the leader,</span>
        <span class="line">seems to have missed his zoology lessons at</span>
        <span class="line">school.</span>
        <span class="line">There is more than one team competing to com-</span>
        <span class="line">plete the quest. Can our odd team beat the lions?</span>
        <span class="line">Who will be faster? Does being faster mean that</span>
        <span class="line">you win? Find out what really matters in the</span>
        <span class="line">end!</span>
      </p>
    </div>

    <div class="code-panel"></div>
  </section>

  <section class="panel panel--front" aria-label="Front cover">
    <div class="painted-ground" role="img" aria-label="Painted background fading from teal and green to red, with soft circles">
      <svg viewBox="0 0 596 849" aria-hidden="true">
        <rect x="0" y="0" width="596" height="30" fill="#1a9a6a"/>
        <circle cx="548" cy="308" r="60" fill="var(--mist)" opacity=".85"/>
        <circle cx="-4" cy="736" r="96" fill="#7fbf9a" opacity=".55"/>
      </svg>
    </div>

    <div class="credits">
      <div class="role">Written by: Tilda Vorhagen</div>
      <div class="role">Illustrated by: Celeste Marina Dunn</div>
    </div>

    <div class="illustration illustration--giraffe" role="img" aria-label="Watercolour illustration of a giraffe's head in close-up"></div>

    <div class="rule rule--front-top"></div>
    <h2 class="title title--front"><span>Captain</span><span class="line-two">Pebble</span></h2>
    <div class="rule rule--front-bottom"></div>

    <div class="illustration illustration--mouse" role="img" aria-label="Watercolour illustration of a small mouse standing in the grass"></div>
  </section>

</main>
</body>
</html>
```